Business Card Design

Freelance writer, coach, teacher and researcher specialising in improving mathematics teaching and learning in primary schools. I write books and articles for teachers, speak extensively at conferences in UK and aboard. Would like something with a cube in the design. Clean, modern - logo suitable for use on a website. Should NOT look 'childish' (no comic sans or chalkboard type fonts)

Full details to go on card:

Professor Dan Theroll
Unlocking Early Numeracy

info@dantheroll.net
#dantheroll26
www.dantheroll.net
+44 7812 660 394

Industry/Entity Type

Teacher

Contact Information for Business Card

Professor Dan Theroll
Unlocking Early Numbers

```html
<!DOCTYPE html>
<html lang="en">
<head>
<meta charset="utf-8">
<title>Professor Dan Theroll – Business Card</title>
<link href="https://fonts.googleapis.com/css2?family=Noto+Serif:wght@400&display=swap" rel="stylesheet">
<style>
  :root {
    --card-black: #000000;
    --card-yellow: #ffce0a;
    --icon-blue: #2c3b8f;
    --ink: #111111;
    --frame-grey: #333333;
    --rule-grey: #a89a4a;
    --mark-deep: #2d3590;
    --mark-violet: #6a52a8;
    --mark-pale: #d4cde8;
  }
  html, body {
    margin: 0;
    padding: 0;
    overflow: hidden;
    background: var(--card-black);
  }
  .card {
    position: relative;
    width: 1200px;
    height: 678px;
    background: var(--card-black);
    font-family: "Noto Serif", Georgia, serif;
    color: var(--ink);
    overflow: hidden;
  }
  .contact-row {
    position: absolute;
    left: 25px;
    width: 662px;
    height: 201px;
    background: var(--card-yellow);
  }
  .contact-row--phone { top: 20px; }
  .contact-row--web { top: 236px; }
  .contact-row--social { top: 450px; }
  .contact-icon {
    position: absolute;
    left: 39px;
    top: 39px;
    width: 124px;
    height: 124px;
    background: var(--icon-blue);
  }
  .contact-icon svg {
    position: absolute;
    left: 31px;
    top: 31px;
    width: 62px;
    height: 62px;
  }
  .contact-text {
    position: absolute;
    left: 201px;
    top: 0;
    height: 201px;
    display: flex;
    flex-direction: column;
    justify-content: center;
    margin: 0;
    font-size: 29px;
    line-height: 1.15;
    letter-spacing: 2.2px;
  }
  .contact-row--phone .contact-text { letter-spacing: 1px; }
  .identity-panel {
    position: absolute;
    left: 704px;
    top: 20px;
    width: 478px;
    height: 631px;
    background: var(--card-yellow);
  }
  .identity-frame {
    position: absolute;
    left: 13px;
    top: 18px;
    width: 444px;
    height: 595px;
    border: 4px solid var(--frame-grey);
  }
  .brand-mark {
    position: absolute;
    left: 47px;
    top: 32px;
    width: 353px;
    height: 322px;
    background: linear-gradient(160deg, var(--mark-deep) 0%, var(--mark-violet) 55%, var(--mark-pale) 100%);
  }
  .identity-name {
    position: absolute;
    left: 0;
    right: 0;
    top: 381px;
    margin: 0;
    text-align: center;
    font-weight: 400;
    font-size: 37px;
    letter-spacing: 1.6px;
  }
  .identity-rule {
    position: absolute;
    left: 62px;
    right: 62px;
    top: 439px;
    height: 1px;
    background: var(--rule-grey);
  }
  .identity-tagline {
    position: absolute;
    left: 0;
    right: 0;
    top: 449px;
    margin: 0;
    text-align: center;
    font-size: 21px;
    letter-spacing: 0.8px;
  }
</style>
</head>
<body>
<main class="card">
  <section class="contact-row contact-row--phone">
    <div class="contact-icon">
      <svg viewBox="0 0 24 24" aria-hidden="true">
        <path fill="#ffce0a" d="M6.6 2.2c.6-.4 1.4-.3 1.8.3l2.3 3.4c.4.6.3 1.4-.2 1.8L9 9c.9 2.2 3.6 5 6 6l1.3-1.5c.5-.5 1.2-.6 1.8-.2l3.4 2.3c.6.4.7 1.2.3 1.8l-1.5 2.1c-.6.9-1.7 1.3-2.7 1C10.5 18.6 5.4 13.5 3.5 6.4c-.3-1 .1-2.1 1-2.7z"/>
      </svg>
    </div>
    <p class="contact-text">+ 44 (7812) 660 394</p>
  </section>

  <section class="contact-row contact-row--web">
    <div class="contact-icon">
      <svg viewBox="0 0 24 24" aria-hidden="true" fill="none" stroke="#ffce0a" stroke-width="1.8">
        <circle cx="12" cy="12" r="10"/>
        <ellipse cx="12" cy="12" rx="4.5" ry="10"/>
        <line x1="12" y1="2" x2="12" y2="22"/>
        <line x1="2" y1="12" x2="22" y2="12"/>
        <line x1="3.5" y1="7" x2="20.5" y2="7"/>
        <line x1="3.5" y1="17" x2="20.5" y2="17"/>
      </svg>
    </div>
    <p class="contact-text"><span>info@dantheroll.net</span><span>www.dantheroll.net</span></p>
  </section>

  <section class="contact-row contact-row--social">
    <div class="contact-icon" aria-hidden="true"></div>
    <p class="contact-text">dantheroll26</p>
  </section>

  <section class="identity-panel">
    <div class="identity-frame">
      <div class="brand-mark" role="img" aria-label="Faceted cube logo mark in blue and violet tones"></div>
      <h1 class="identity-name">Professor Dan Theroll</h1>
      <div class="identity-rule"></div>
      <p class="identity-tagline">Unlocking Early Numeracy</p>
    </div>
  </section>
</main>
</body>
</html>
```